Real eatate

My company name is “Maple Crest Realestate” i would like to create a business card. I would like something modern and sleek similar to picture uploaded. All text in the business card should be black and the logo gold any shade.

```html
<!DOCTYPE html>
<html lang="en">
<head>
<meta charset="utf-8">
<title>Maple Crest Realestate – Business Card</title>
<link rel="stylesheet" href="https://fonts.googleapis.com/css2?family=Montserrat:wght@500;600;700&display=swap">
<style>
  :root {
    --backdrop: #b9b9b9;
    --card: #1f1e1e;
    --card-sheen: #2b2a2a;
    --gold: #d2b077;
    --gold-soft: #c3a26c;
  }
  * { box-sizing: border-box; margin: 0; padding: 0; }
  html, body { width: 1200px; height: 675px; overflow: hidden; }
  body {
    background: var(--backdrop);
    font-family: "Montserrat", Arial, sans-serif;
    display: flex;
    align-items: center;
    justify-content: center;
    gap: 60px;
  }
  .card {
    position: relative;
    width: 500px;
    height: 286px;
    border-radius: 14px;
    background: linear-gradient(115deg, var(--card) 0%, var(--card-sheen) 45%, var(--card) 100%);
    color: var(--gold);
    box-shadow: 0 10px 28px rgba(0,0,0,.28);
  }

  /* Front */
  .card--front {
    display: flex;
    flex-direction: column;
    align-items: center;
    justify-content: center;
    gap: 22px;
  }
  .brand-dot {
    width: 64px; height: 64px;
    border-radius: 50%;
    background: var(--gold);
  }
  .brand-name {
    font-weight: 600;
    font-size: 22px;
    letter-spacing: 1.5px;
    text-transform: uppercase;
    text-align: center;
    line-height: 1.25;
    max-width: 300px;
  }

  /* Back */
  .card--back { padding: 30px 34px; }
  .back-brand {
    position: absolute;
    top: 34px; left: 34px;
    display: flex; align-items: center; gap: 14px;
  }
  .back-brand .brand-dot { width: 40px; height: 40px; }
  .back-brand .brand-name { font-size: 15px; text-align: left; max-width: 200px; }
  .divider {
    position: absolute;
    left: 34px; right: 34px; top: 120px;
    height: 1.5px;
    background: var(--gold-soft);
  }
  .contact {
    position: absolute;
    top: 140px;
    list-style: none;
    display: flex; flex-direction: column; gap: 12px;
    font-size: 12px; font-weight: 500;
  }
  .contact--left { left: 34px; }
  .contact--right { left: 200px; top: 190px; }
  .contact li { display: flex; align-items: center; gap: 8px; }
  .contact svg { width: 12px; height: 12px; fill: var(--gold); }
  .person {
    position: absolute;
    right: 34px; bottom: 30px;
    text-align: left;
    border-bottom: 1.5px solid var(--gold-soft);
    padding: 0 18px 6px 0;
  }
  .person-name { font-size: 22px; font-weight: 700; letter-spacing: .5px; }
  .person-title { font-size: 10px; font-weight: 500; }
</style>
</head>
<body>
  <section class="card card--front">
    <span class="brand-dot" aria-hidden="true"></span>
    <h1 class="brand-name">Maple Crest Realestate</h1>
  </section>

  <section class="card card--back">
    <div class="back-brand">
      <span class="brand-dot" aria-hidden="true"></span>
      <span class="brand-name">Maple Crest Realestate</span>
    </div>
    <div class="divider"></div>
    <ul class="contact contact--left">
      <li><svg viewBox="0 0 24 24"><path d="M12 2a7 7 0 0 0-7 7c0 5 7 13 7 13s7-8 7-13a7 7 0 0 0-7-7zm0 9.5A2.5 2.5 0 1 1 12 6.5a2.5 2.5 0 0 1 0 5z"/></svg>Address</li>
      <li><svg viewBox="0 0 24 24"><path d="M6.6 10.8a15 15 0 0 0 6.6 6.6l2.2-2.2a1 1 0 0 1 1-.25 11.4 11.4 0 0 0 3.6.6 1 1 0 0 1 1 1V20a1 1 0 0 1-1 1A17 17 0 0 1 3 4a1 1 0 0 1 1-1h3.5a1 1 0 0 1 1 1c0 1.25.2 2.45.6 3.6a1 1 0 0 1-.25 1z"/></svg>Phone number</li>
    </ul>
    <ul class="contact contact--right">
      <li><svg viewBox="0 0 24 24"><path d="M3 5h18v14H3zm2 2v.5l7 4.5 7-4.5V7l-7 4.5z"/></svg>E-mail</li>
      <li><svg viewBox="0 0 24 24"><path d="M12 2a10 10 0 1 0 0 20 10 10 0 0 0 0-20zm6.9 9h-3a15 15 0 0 0-1.3-5.4A8 8 0 0 1 18.9 11zM12 4c.9 1.2 1.8 3.5 2 7h-4c.2-3.5 1.1-5.8 2-7zM9.4 5.6A15 15 0 0 0 8.1 11h-3a8 8 0 0 1 4.3-5.4zM5.1 13h3a15 15 0 0 0 1.3 5.4A8 8 0 0 1 5.1 13zm6.9 7c-.9-1.2-1.8-3.5-2-7h4c-.2 3.5-1.1 5.8-2 7zm2.6-1.6a15 15 0 0 0 1.3-5.4h3a8 8 0 0 1-4.3 5.4z"/></svg>Website</li>
    </ul>
    <div class="person">
      <div class="person-name">NAME</div>
      <div class="person-title">Designation</div>
    </div>
  </section>
</body>
</html>
```